Clear Plastic Card Design

I am looking to have a business card designed from my logo icon. I am looking to match the style of a different business card I have attached in the files.
Looking for a card that is plastic, with layers of transparency in the shape of my logo icon (also attached in the files) - not a circle like the other card. The winning design will incorporate the red icon logo on the front and back and include the charity's name, "Lanterns of Willow Creek" in the same or similar font, as well as an email and phone number. For now, use the email: email@lanternsofwillowcreek.org and the phone number 555-014-7392.
We like how the sample business card has transparency, partial and full opacity layers and a matching color scheme. Files will need to be in vector so that our business card printing company can work with it.
UPDATE:
We've some excellent designs in, thank you everyone! I got an early review from the owner, and he requested a minor redirect to find his perfect design. He wants the design to stand out by NOT being a rectangle. Try instead a circle, square, or best yet - something that falls in the outline of the logo icon, either fully or partially. Thank you, everyone!
Lanterns of Willow Creek text should be incorporated as well as a phone and email.

```html
<!DOCTYPE html>
<html lang="en">
<head>
<meta charset="utf-8">
<title>Lanterns of Willow Creek — Business Card</title>
<link rel="stylesheet" href="https://fonts.googleapis.com/css2?family=Questrial&family=Roboto:wght@400&display=swap">
<style>
  :root {
    --backdrop: #d9d4cc;
    --card-frost: #ece9e4;
    --card-edge: #f7f6f3;
    --ink: #333333;
    --ink-soft: #4a4a4a;
    --brand-red: #c0262d;
    --brand-red-deep: #9c1620;
    --band-dark: #1e1e1e;
    --band-text: #f3e9e9;
  }
  * { margin: 0; padding: 0; box-sizing: border-box; }
  html, body {
    width: 1200px;
    height: 969px;
    overflow: hidden;
    background: var(--backdrop);
  }
  .canvas {
    position: relative;
    width: 1200px;
    height: 969px;
  }
  .card {
    position: absolute;
    left: 80px;
    top: 187px;
    width: 1040px;
    height: 594px;
    background: linear-gradient(160deg, var(--card-edge) 0%, var(--card-frost) 55%, #e4e0da 100%);
    border: 1px solid rgba(255,255,255,0.7);
    box-shadow: 0 4px 14px rgba(0,0,0,0.12);
    overflow: hidden;
  }
  .brand {
    position: absolute;
    left: 91px;
    top: 100px;
    display: flex;
    align-items: flex-end;
    gap: 18px;
  }
  .brand-name {
    font-family: "Questrial", sans-serif;
    font-size: 31px;
    line-height: 1.22;
    color: var(--ink);
  }
  .brand-mark {
    width: 150px;
    height: 150px;
    background: linear-gradient(135deg, var(--brand-red) 0%, #d9481c 100%);
  }
  .contact {
    position: absolute;
    left: 95px;
    top: 404px;
    list-style: none;
    font-family: "Roboto", sans-serif;
    font-size: 23px;
    color: var(--ink-soft);
  }
  .contact li {
    display: flex;
    align-items: center;
    gap: 14px;
    height: 31px;
  }
  .contact svg { width: 20px; height: 20px; fill: var(--brand-red); flex: none; }
  .footer-band {
    position: absolute;
    left: 0;
    bottom: 0;
    width: 100%;
    height: 50px;
  }
  .footer-band svg { position: absolute; inset: 0; }
  .website {
    position: absolute;
    right: 38px;
    bottom: 8px;
    font-family: "Roboto", sans-serif;
    font-size: 24px;
    color: var(--band-text);
  }
</style>
</head>
<body>
<main class="canvas">
  <section class="card" aria-label="Business card front">
    <div class="brand">
      <p class="brand-name">Lanterns of the<br>Willow Creek</p>
      <div class="brand-mark" aria-hidden="true"></div>
    </div>

    <ul class="contact">
      <li>
        <svg viewBox="0 0 24 24" aria-hidden="true"><path d="M6.6 10.8c1.4 2.8 3.8 5.1 6.6 6.6l2.2-2.2c.3-.3.7-.4 1-.2 1.1.4 2.3.6 3.6.6.6 0 1 .4 1 1V20c0 .6-.4 1-1 1C10.6 21 3 13.4 3 4c0-.6.4-1 1-1h3.5c.6 0 1 .4 1 1 0 1.3.2 2.5.6 3.6.1.3 0 .7-.2 1z"/></svg>
        <span>555-014-7392</span>
      </li>
      <li>
        <svg viewBox="0 0 24 24" aria-hidden="true"><path d="M2 5h20v14H2z M2 5l10 8 10-8" fill="var(--brand-red)"/><path d="M3 6l9 7 9-7" fill="none" stroke="#ece9e4" stroke-width="1.6"/></svg>
        <span>email@lanternsofwillowcreek.org</span>
      </li>
    </ul>

    <div class="footer-band">
      <svg width="1040" height="50" viewBox="0 0 1040 50" aria-hidden="true">
        <defs>
          <linearGradient id="band-red" x1="0" x2="1" y1="0" y2="0">
            <stop offset="0" stop-color="var(--brand-red)"/>
            <stop offset="1" stop-color="var(--brand-red-deep)"/>
          </linearGradient>
        </defs>
        <rect x="0" y="28" width="620" height="22" fill="var(--band-dark)"/>
        <polygon points="622,50 666,0 1040,0 1040,50" fill="url(#band-red)"/>
      </svg>
      <span class="website">lanternsofwillowcreek.org</span>
    </div>
  </section>
</main>
</body>
</html>
```